Web design for Vantor Ledgerly

We need to redesign and update the website for www.vantorledgerly.io, if you'll look, you can see it is very poorly done.

The content won't change much (the founders page will go away though). I've attached a logo and flyer we are using that may provide inspiration for the design, though you don't have to make it consistent with the flyer.

Industry/Entity Type

Hr technology

Coding

Coded - Design and coding required

Number of Pages Required

5+ page

Requirements
Must have
• To be hosted with NestHarbor

```html
<!DOCTYPE html>
<html lang="en">
<head>
<meta charset="utf-8">
<title>Vantor Ledgerly – HR Analytics Platform</title>
<link href="https://fonts.googleapis.com/css2?family=Josefin+Sans:wght@400;600;700&family=Lato:wght@400;700&display=swap" rel="stylesheet">
<style>
:root{
  --navy:#1d4487;
  --sky:#84c9e8;
  --amber:#f5ac21;
  --ink:#2a2a2a;
  --card:#f4f4f4;
  --line:#dcdcdc;
  --black:#050505;
  --white:#fff;
}
*{box-sizing:border-box;margin:0;padding:0}
html,body{width:1200px;height:3380px;overflow:hidden;background:var(--white)}
body{position:relative;font-family:'Lato',sans-serif;color:var(--ink)}
.abs{position:absolute}

/* header */
.site-header{position:absolute;left:0;top:0;width:1200px;height:120px;background:var(--white)}
.brand{position:absolute;left:75px;top:44px;display:flex;align-items:center;gap:10px;font-family:'Josefin Sans',sans-serif;font-weight:700;font-size:24px;color:var(--navy)}
.brand-dot{width:30px;height:30px;border-radius:50%;background:var(--amber)}
.main-nav{position:absolute;left:424px;top:55px;display:flex;gap:39px;font-family:'Josefin Sans',sans-serif;font-size:13.5px;color:#333}
.main-nav a{color:inherit;text-decoration:none}
.main-nav .active{color:var(--navy);font-weight:700;padding-bottom:6px;border-bottom:2px solid var(--navy)}
.quote-btn{position:absolute;left:966px;top:42px;width:158px;height:40px;border-radius:20px;background:linear-gradient(100deg,var(--navy) 0 68%,var(--amber) 68%);color:#fff;font-family:'Josefin Sans',sans-serif;font-size:13.5px;display:flex;align-items:center;padding-left:17px;gap:10px}

/* hero */
.hero{position:absolute;left:0;top:120px;width:1200px;height:740px;background:var(--sky);overflow:hidden}
.hero-art{position:absolute;left:416px;top:130px;width:740px;height:590px;border-radius:30px;background:radial-gradient(ellipse at 55% 55%,#5fb2e6 0%,#9fd5ee 60%,rgba(132,201,232,0) 80%)}
.hero-cloud{position:absolute;left:0;top:560px}
.hero-shadow{position:absolute;left:32px;top:193px;width:415px;height:232px;background:#a9d2c6;opacity:.6}
.hero-box{position:absolute;left:47px;top:211px;width:413px;height:232px;background:var(--amber);padding:24px 0 0 33px}
.hero-box h1{font-family:'Josefin Sans',sans-serif;font-weight:700;font-size:36px;line-height:45px;color:var(--navy);white-space:nowrap}

/* about */
.section-title{position:absolute;width:1200px;text-align:center;font-family:'Josefin Sans',sans-serif;font-weight:700}
.about-title{top:930px;font-size:35px;color:#333}
.about-title::after{content:"";display:block;width:70px;height:3px;background:#666;margin:8px auto 0}
.about-visual{position:absolute;left:143px;top:972px;width:420px;height:420px;border-radius:50%;background:radial-gradient(circle at 50% 45%,#fbfcff 0%,#e6ebf6 70%,#dce4f3 100%)}
.about-text{position:absolute;left:616px;top:1022px;width:466px;font-size:13.4px;line-height:22px;color:#333}
.about-text p+p{margin-top:22px}
.pill{position:absolute;border-radius:22px;background:var(--navy);color:#fff;font-size:13px;display:flex;align-items:center;justify-content:center}
.read-more{left:618px;top:1308px;width:155px;height:39px}

/* provide */
.provide{position:absolute;left:0;top:1510px;width:1200px;height:938px;background:var(--amber)}
.provide-title{top:1582px;font-size:36px;color:#fff}
.provide-sub{position:absolute;top:1623px;width:1176px;text-align:center;font-size:13px;line-height:16px;color:#fff}
.card{position:absolute;width:307px;height:319px;background:var(--card);text-align:center}
.card svg.icon{position:absolute;left:96px;top:30px}
.card h3{position:absolute;left:0;width:100%;top:166px;font-family:'Josefin Sans',sans-serif;font-weight:600;font-size:17.5px;line-height:21px;color:#222;text-transform:uppercase}
.card p{position:absolute;left:20px;width:267px;top:228px;font-size:13px;line-height:16px;color:#444}
.card .go{position:absolute;left:135px;top:268px;width:32px;height:32px;border-radius:50%;background:var(--navy);display:flex;align-items:center;justify-content:center}

/* contact form */
.touch-title{top:2512px;font-size:31px;font-weight:600;color:#222}
.field{position:absolute;border:1px solid var(--line);background:#fff;font-size:12px;color:#999;padding:10px 13px}
.send{left:525px;top:2763px;width:154px;height:39px;font-size:12px}

/* footer */
.footer{position:absolute;left:0;top:2969px;width:1200px;height:360px;background:var(--black)}
.banner{position:absolute;left:270px;top:2868px;width:704px;height:180px;border-radius:42px;background:linear-gradient(120deg,#f6a823,#f39c1d 60%,#f5b030);text-align:center;color:#fff}
.banner p{margin-top:50px;font-size:16.5px;line-height:26px}
.banner .mail{display:flex;justify-content:center;align-items:center;gap:16px;margin-top:10px;font-size:30px}
.foot-brand{position:absolute;left:118px;top:3110px;width:220px;text-align:center;font-family:'Josefin Sans',sans-serif;font-weight:700;font-size:26px;color:#fff}
.foot-brand .ring{display:block;margin:0 auto 14px;width:60px;height:60px;border-radius:50%;background:#8a8a8a}
.foot-col{position:absolute;top:3098px;color:#fff}
.foot-col h4{font-family:'Josefin Sans',sans-serif;font-size:12.5px;font-weight:700;letter-spacing:.3px}
.foot-col h4::after{content:"";display:block;width:38px;height:2px;background:#fff;margin-top:8px}
.foot-col ul{list-style:none;margin-top:14px;font-family:'Josefin Sans',sans-serif;font-size:13.5px;letter-spacing:.6px}
.foot-col li{height:22.5px}
.foot-col li::before{content:">";margin-right:9px}
.foot-col li.on{font-weight:700}
.contact-list{margin-top:14px;font-size:12.5px}
.contact-list div{display:flex;align-items:center;gap:12px;height:45px;margin-top:-11px}
.news-input{position:absolute;left:865px;top:3146px;width:260px;height:40px;border-radius:20px;background:#fff;color:#333;font-size:12.5px;padding:12px 17px}
.subscribe{left:865px;top:3196px;width:260px;height:39px;font-size:12.5px}
.copy-bar{position:absolute;left:0;top:3329px;width:1200px;height:51px;background:#fff}
.copy-bar p{position:absolute;left:112px;top:20px;font-size:12px;color:#333}
.social{position:absolute;top:3342px;width:25px;height:25px;border-radius:50%;background:var(--navy)}
</style>
</head>
<body>

<header class="site-header">
  <div class="brand"><span class="brand-dot"></span>Vantor Ledgerly</div>
  <nav class="main-nav">
    <a class="active">Home</a><a>Our Solutions</a><a>Our Difference</a><a>About Us</a><a>Contact Us</a>
  </nav>
  <div class="quote-btn">Get A Quote
    <svg width="40" height="12" viewBox="0 0 40 12"><path d="M0 6h36M31 1l6 5-6 5" stroke="#fff" stroke-width="2" fill="none"/></svg>
  </div>
</header>

<section class="hero">
  <div class="hero-art" role="img" aria-label="Isometric illustration of people working around data dashboards above a cloud and database stack"></div>
  <svg class="hero-cloud" width="1200" height="180" viewBox="0 0 1200 180">
    <path d="M0 140 C20 90 80 60 140 78 C170 40 240 40 270 70 C300 50 340 60 360 90 C400 60 460 60 490 95 C540 75 600 85 640 110 L700 110 C760 150 900 90 1000 120 C1080 40 1180 20 1200 40 L1200 180 L0 180 Z" fill="#fff"/>
  </svg>
  <div class="hero-shadow"></div>
  <div class="hero-box"><h1>Stop Moving data<br>Between System<br>without Realizing The<br>Value of Insights.</h1></div>
</section>

<h2 class="section-title about-title">ABOUT US</h2>

<div class="about-visual" role="img" aria-label="Illustrated diagram showing ATS and HRIS/Payroll data flowing into the platform and out to KPIs and data visualization"></div>

<div class="about-text">
  <p>Vantor Ledgerly gives you the ablity to make the most of your investment in Payvance and Hirebloom. By providing a seamless method of managing your master data between systems. clients get much than the simple movement of data from one system to another or keeping then is sync. information drives business decisions and by leveraging Vantor Ledgerly's suite of service, clients can quickly access real time information acress multiple systems. information that tradional data connection services move and lose. Every Transaction builds insight that drives value</p>
  <p>Cloud native technologies allow Vantor Ledgerly to extend Services into your organizations, adding value quickly and effectively and can provide immediate ROI.</p>
</div>
<div class="pill read-more">Read More</div>

<section class="provide"></section>
<h2 class="section-title provide-title">WHAT WE PROVIDE</h2>
<p class="provide-sub">What we consider when<br>we create your repository of HR historical data</p>

<div class="card" style="left:113px;top:1686px">
  <svg class="icon" width="115" height="115" viewBox="0 0 115 115" fill="none" stroke="#222" stroke-width="3"><circle cx="57" cy="57" r="40"/><circle cx="57" cy="57" r="26"/><path d="M57 10v10M57 94v10M10 57h10M94 57h10M24 24l7 7M83 83l7 7M24 90l7-7M83 31l7-7"/><path d="M57 42v22M57 54l-10 10M57 54l10 10"/></svg>
  <h3>Streamline application<br>implementation</h3>
  <p>Makes system implementations and upgrades easier with better data quality.</p>
  <div class="go"><svg width="12" height="10" viewBox="0 0 12 10"><path d="M0 5h10M6 1l4 4-4 4" stroke="#fff" stroke-width="2" fill="none"/></svg></div>
</div>
<div class="card" style="left:445px;top:1686px">
  <svg class="icon" width="115" height="115" viewBox="0 0 115 115" fill="none" stroke="#222" stroke-width="3"><circle cx="57" cy="57" r="44"/><circle cx="57" cy="57" r="22"/><circle cx="57" cy="57" r="10"/><path d="M20 30l14 4-4 14M95 84l-14-4 4-14"/></svg>
  <h3>Manage data<br>effectively</h3>
  <p>Effective data management requires expert skills and experience.</p>
  <div class="go"><svg width="12" height="10" viewBox="0 0 12 10"><path d="M0 5h10M6 1l4 4-4 4" stroke="#fff" stroke-width="2" fill="none"/></svg></div>
</div>
<div class="card" style="left:779px;top:1686px">
  <svg class="icon" width="115" height="115" viewBox="0 0 115 115" fill="none" stroke="#222" stroke-width="3"><rect x="24" y="12" width="52" height="90" rx="6"/><path d="M24 88h52M46 95h8M40 48l8 8 14-14"/><path d="M70 62l18 6v14c0 9-8 14-18 18-10-4-18-9-18-18V68z" fill="#f4f4f4"/></svg>
  <h3 style="top:176px">Future proof</h3>
  <p>New innovations keep you ahead of your competitors.</p>
  <div class="go"><svg width="12" height="10" viewBox="0 0 12 10"><path d="M0 5h10M6 1l4 4-4 4" stroke="#fff" stroke-width="2" fill="none"/></svg></div>
</div>
<div class="card" style="left:113px;top:2031px">
  <svg class="icon" width="115" height="115" viewBox="0 0 115 115" fill="none" stroke="#222" stroke-width="3"><circle cx="57" cy="18" r="10"/><circle cx="57" cy="66" r="14"/><circle cx="22" cy="76" r="9"/><circle cx="92" cy="76" r="9"/><path d="M8 110v-12a8 8 0 018-8h12a8 8 0 018 8v12zM78 110v-12a8 8 0 018-8h12a8 8 0 018 8v12zM44 38h26M24 62c2-14 10-22 20-26M90 62c-2-14-10-22-20-26"/></svg>
  <h3>Model your<br>organization</h3>
  <p style="top:218px">Model the way your organization really is, not the way your vendor sees it.</p>
  <div class="go" style="left:141px;top:272px"><svg width="12" height="10" viewBox="0 0 12 10"><path d="M0 5h10M6 1l4 4-4 4" stroke="#fff" stroke-width="2" fill="none"/></svg></div>
</div>
<div class="card" style="left:445px;top:2031px">
  <svg class="icon" width="115" height="115" viewBox="0 0 115 115" fill="none" stroke="#222" stroke-width="3"><circle cx="57" cy="55" r="46"/><circle cx="57" cy="55" r="30"/><circle cx="57" cy="46" r="11"/><path d="M40 78c2-12 8-18 17-18s15 6 17 18M57 62v20"/></svg>
  <h3>Gain insights into<br>your workforce</h3>
  <p style="top:218px">Provides the platform for strategic analytics and machine learning.</p>
  <div class="go" style="left:137px;top:272px"><svg width="12" height="10" viewBox="0 0 12 10"><path d="M0 5h10M6 1l4 4-4 4" stroke="#fff" stroke-width="2" fill="none"/></svg></div>
</div>
<div class="card" style="left:779px;top:2031px">
  <svg class="icon" width="115" height="115" viewBox="0 0 115 115" fill="none" stroke="#222" stroke-width="3"><path d="M24 56c-12 0-16-18-2-22 0-18 22-26 34-14 8-16 36-10 36 8 14 0 16 22 2 24"/><circle cx="57" cy="66" r="16"/><circle cx="57" cy="66" r="6"/><circle cx="26" cy="84" r="3"/><circle cx="40" cy="88" r="3"/><circle cx="34" cy="100" r="3"/></svg>
  <h3>Leverage cloud-native<br>capabilities</h3>
  <p style="top:218px">Focus on the needs of your business, not the technology.</p>
  <div class="go" style="left:131px;top:272px"><svg width="12" height="10" viewBox="0 0 12 10"><path d="M0 5h10M6 1l4 4-4 4" stroke="#fff" stroke-width="2" fill="none"/></svg></div>
</div>

<h2 class="section-title touch-title">Get in Touch</h2>
<div class="field" style="left:282px;top:2571px;width:206px;height:42px">Name*</div>
<div class="field" style="left:498px;top:2571px;width:206px;height:42px">Phone*</div>
<div class="field" style="left:713px;top:2571px;width:206px;height:42px">Email*</div>
<div class="field" style="left:282px;top:2622px;width:637px;height:116px">Message</div>
<div class="pill send">Send</div>

<footer class="footer"></footer>
<div class="banner">
  <p>Let us do the heavy lifting so you can focus on what<br>matters most to your business</p>
  <div class="mail">
    <svg width="40" height="32" viewBox="0 0 40 32"><rect x="1" y="4" width="38" height="27" rx="2" fill="#1d4487"/><path d="M1 5l19 14 19-14" stroke="#fff" stroke-width="2" fill="none"/></svg>
    sales@vantorledgerly.io
  </div>
</div>

<div class="foot-brand"><span class="ring"></span>Vantor Ledgerly</div>

<div class="foot-col" style="left:435px">
  <h4>QUICK LINKS</h4>
  <ul><li class="on">Home</li><li>Our Solutions</li><li>Our Difference</li><li>About Us</li><li>Contact Us</li></ul>
</div>
<div class="foot-col" style="left:618px">
  <h4>CONTACT INFO</h4>
  <div class="contact-list">
    <div><svg width="12" height="12" viewBox="0 0 12 12"><path d="M2 1l3 1 1 3-2 1c1 2 2 3 4 4l1-2 3 1 0 3c-6 0-10-4-10-10z" fill="#fff"/></svg>123 456 7890</div>
    <div><svg width="13" height="10" viewBox="0 0 13 10"><rect width="13" height="10" fill="#fff"/><path d="M0 0l6.5 5L13 0" stroke="#000" fill="none"/></svg>www.vantorledgerly.io</div>
    <div><svg width="12" height="14" viewBox="0 0 12 14"><path d="M6 0a5 5 0 015 5c0 4-5 9-5 9S1 9 1 5a5 5 0 015-5z" fill="#fff"/><circle cx="6" cy="5" r="2" fill="#000"/></svg>Alderwick, SK</div>
  </div>
</div>
<div class="foot-col" style="left:865px"><h4>NEWSLETTER</h4></div>
<div class="news-input">Email address</div>
<div class="pill subscribe">Subscribe</div>

<div class="copy-bar"><p>Copyright © 2022 Vantor Ledgerly. All Rights Reserved</p></div>
<div class="social" style="left:999px"></div>
<div class="social" style="left:1033px"></div>
<div class="social" style="left:1067px"></div>
<div class="social" style="left:1100px"></div>

</body>
</html>
```